Web site design for Brivolt Software (www.brivoltsoftware-example.com)

Need the design as well as the html for the website. The brief is given in the attached file.
If possible, would like to use pencil sketches instead of images to give a unique look to the site.
Target Market(s)
small Software product companies
Industry/Entity Type
Software
Coding
Coded - Design and coding required
Number of Pages Required
5+ page

```html
<!DOCTYPE html>
<html lang="en">
<head>
<meta charset="utf-8">
<title>Brivolt Software</title>
<link rel="stylesheet" href="https://fonts.googleapis.com/css2?family=Ropa+Sans&family=PT+Sans:wght@400;700&display=swap">
<style>
:root{
  --red:#c8141c;
  --red-band:#d54a4e;
  --red-foot:#d5474b;
  --ink:#222;
  --muted:#7a7a7a;
  --dark:#1d1d1d;
  --white:#fff;
  --line:#e2e2e2;
}
*{box-sizing:border-box;margin:0;padding:0}
html,body{width:1200px;height:3141px;overflow:hidden}
body{position:relative;background:var(--white);font-family:"PT Sans",Arial,sans-serif;color:var(--ink)}
.abs{position:absolute}
/* top bar */
.topbar{left:0;top:0;width:1200px;height:42px;background:var(--white)}
.phone{left:199px;top:12px;font-size:13px;color:var(--muted);display:flex;align-items:center;gap:8px}
.brand{left:430px;top:4px;width:340px;text-align:center;font-family:"Ropa Sans",sans-serif;font-size:30px;letter-spacing:5px;color:#333;text-transform:uppercase}
.social-top{left:908px;top:13px;display:flex;gap:10px}
.social-top span{width:12px;height:12px;border-radius:50%;background:#9a9a9a}
/* hero */
.hero{left:0;top:42px;width:1200px;height:608px;clip-path:polygon(0 0,100% 0,100% 471px,0 100%);
  background:linear-gradient(120deg,#3d4245 0%,#2a2e31 40%,#575b5d 70%,#2c2f31 100%)}
.nav{left:0;top:42px;width:1200px;height:46px;background:rgba(10,10,10,.75);display:flex;justify-content:center;gap:31px;align-items:center}
.nav a{color:var(--white);font-size:13.5px;font-weight:700;text-decoration:none}
.hero-title{left:199px;top:236px;font-family:"Ropa Sans",sans-serif;font-size:47px;line-height:60px;color:var(--white);letter-spacing:1px}
.btn-ghost{height:42px;border:2px solid var(--white);color:var(--white);font-family:"Ropa Sans",sans-serif;font-size:17px;letter-spacing:1px;display:flex;align-items:center;justify-content:center;gap:10px}
.arrow-box{top:300px;width:42px;height:32px;border:2px solid var(--white);display:flex;align-items:center;justify-content:center}
/* section headings */
.sec-title{left:199px;font-family:"Ropa Sans",sans-serif;font-size:32px;color:var(--ink);display:flex;align-items:center;gap:16px}
.sec-title::after{content:"";width:56px;height:3px;background:var(--red)}
.sec-title.light{color:var(--white)}
.sec-title.light::after{background:var(--white)}
.sec-sub{left:199px;font-size:14px;font-weight:700;color:#555}
.sec-sub.light{color:var(--white)}
/* services */
.svc{top:808px;width:249px;height:193px;text-align:center;padding-top:18px}
.svc.active{border:1px solid var(--line);border-bottom:3px solid var(--red);box-shadow:0 2px 6px rgba(0,0,0,.12)}
.ico-circle{width:56px;height:56px;border-radius:50%;background:var(--red);margin:0 auto;display:flex;align-items:center;justify-content:center}
.svc h3{font-size:14px;font-weight:700;margin-top:14px;color:var(--ink)}
.svc p{font-size:11.5px;line-height:18px;color:var(--muted);margin:8px auto 0;width:200px}
.btn-red{background:var(--red);color:var(--white);font-size:12px;font-weight:700;display:flex;align-items:center;justify-content:center;gap:8px;box-shadow:0 3px 0 #8d0e13}
/* background band */
.band{left:0;top:1158px;width:1200px;height:402px;background:var(--red-band);clip-path:polygon(0 0,100% 0,100% 333px,0 100%)}
.band-text{left:199px;top:1302px;width:800px;font-size:11.5px;line-height:24px;color:var(--white)}
.btn-white{background:var(--white);color:var(--red);font-size:12px;font-weight:700;display:flex;align-items:center;justify-content:center;gap:8px;box-shadow:0 3px 0 #3a3a3a}
/* engagement */
.eng{top:1711px;width:270px;display:flex;gap:12px}
.eng-ico{width:73px;height:73px;background:var(--red);flex:none;display:flex;align-items:center;justify-content:center}
.eng h3{font-size:14px;font-weight:700;margin-top:2px}
.eng p{font-size:11.5px;line-height:17px;color:var(--muted);margin-top:4px}
/* case studies */
.cases{left:0;top:1874px;width:1200px;height:507px;clip-path:polygon(0 0,100% 0,100% 429px,0 100%);
  background:linear-gradient(100deg,#5a5a5a 0%,#4a4a4a 35%,#2a2a2a 55%,#6d6d6d 80%,#4f4f4f 100%)}
.case{top:2069px;height:134px;border:1px solid rgba(255,255,255,.75);padding:26px 22px 0 20px;display:flex;gap:14px;color:var(--white)}
.case h3{font-size:11.5px;font-weight:700;text-transform:uppercase}
.case p{font-size:11.5px;line-height:20px;margin-top:8px}
.case .more{font-size:11.5px;font-weight:700;margin-top:4px;display:flex;gap:8px;align-items:center}
.dots{left:586px;top:2241px;display:flex;gap:4px}
.dots span{width:8px;height:8px;background:var(--white)}
.dots span.on{background:var(--red)}
/* blog */
.post{top:2555px;width:250px;height:184px;border:1px solid #dcdcdc;text-align:center}
.post-tab{position:absolute;left:95px;top:-10px;width:60px;height:40px;background:var(--white);display:flex;justify-content:center;align-items:center}
.post p{font-size:12px;line-height:21px;margin:55px auto 0;width:210px;font-weight:700;color:#333}
.post hr{width:40px;border:0;height:2px;background:var(--red);margin:6px auto}
.post .date{font-size:15px;font-style:italic;color:#555}
/* footer */
.footer{left:0;top:2852px;width:1200px;height:253px;background:var(--red-foot);color:var(--white)}
.foot-h{font-size:14px;font-weight:700}
.foot-p{font-size:10.5px;line-height:18px}
.foot-list{list-style:none;font-size:10.5px;line-height:23.5px}
.foot-list li::before{content:"→";margin-right:10px}
.soc-list{list-style:none;font-size:10.5px}
.soc-list li{display:flex;align-items:center;gap:10px;height:27px}
.soc-list li span{width:20px;height:20px;border:1px solid var(--white)}
.copy{left:0;top:3105px;width:1200px;height:36px;background:#151515;color:var(--white);font-size:11.5px;text-align:center;line-height:36px}
</style>
</head>
<body>

<header class="abs topbar">
  <div class="abs phone">
    <svg width="12" height="12" viewBox="0 0 24 24"><path fill="#c8141c" d="M6.6 10.8a15 15 0 006.6 6.6l2.2-2.2c.3-.3.7-.4 1-.2 1.1.4 2.3.6 3.6.6.6 0 1 .4 1 1V20c0 .6-.4 1-1 1A17 17 0 013 4c0-.6.4-1 1-1h3.5c.6 0 1 .4 1 1 0 1.3.2 2.5.6 3.6.1.3 0 .7-.2 1z"/></svg>
    +65 (0) 1200 555 014
  </div>
  <div class="abs brand">Brivolt Software</div>
  <div class="abs social-top"><span></span><span></span><span></span><span></span></div>
</header>

<section class="abs hero" role="img" aria-label="Photo of a developer working at a desk with code on monitors"></section>
<nav class="abs nav">
  <a href="#">Home</a><a href="#">About us</a><a href="#">Services</a><a href="#">Expertise</a><a href="#">Engagement Models</a><a href="#">Case Studies</a><a href="#">Work With Us</a><a href="#">Blog</a><a href="#">Contact</a>
</nav>
<h1 class="abs hero-title">Infecting Engineering<br>With Design</h1>
<a class="abs btn-ghost" style="left:199px;top:400px;width:158px">READ MORE
  <svg width="16" height="10" viewBox="0 0 16 10"><path d="M0 5h13M9 1l4 4-4 4" stroke="#fff" stroke-width="2" fill="none"/></svg></a>
<a class="abs btn-ghost" style="left:377px;top:400px;width:156px">CONTACT US
  <svg width="16" height="14" viewBox="0 0 16 14"><path d="M1 12c2-5 5-8 8-9M9 1l3 2-2 3" stroke="#fff" stroke-width="2" fill="none"/></svg></a>
<div class="abs arrow-box" style="left:4px"><svg width="20" height="12" viewBox="0 0 20 12"><path d="M20 6H3M8 1 3 6l5 5" stroke="#fff" stroke-width="2" fill="none"/></svg></div>
<div class="abs arrow-box" style="left:1154px"><svg width="20" height="12" viewBox="0 0 20 12"><path d="M0 6h17M12 1l5 5-5 5" stroke="#fff" stroke-width="2" fill="none"/></svg></div>

<!-- services -->
<h2 class="abs sec-title" style="top:698px">Our Services</h2>
<p class="abs sec-sub" style="top:740px">Perfection is achieved not when there is nothing more to add</p>

<div class="abs svc active" style="left:199px">
  <div class="ico-circle"><svg width="28" height="28" viewBox="0 0 24 24"><path d="M12 2 3 7v10l9 5 9-5V7zM3 7l9 5 9-5M12 12v10" stroke="#fff" stroke-width="1.6" fill="none"/></svg></div>
  <h3>BUILD PRODUCT</h3>
  <p>Our team of analysts, design thinkers and technologists work with client and end carve out a product.</p>
</div>
<div class="abs svc" style="left:476px">
  <div class="ico-circle"><svg width="28" height="28" viewBox="0 0 24 24"><circle cx="12" cy="12" r="4" stroke="#fff" stroke-width="2" fill="none"/><circle cx="12" cy="12" r="8.5" stroke="#fff" stroke-width="3" stroke-dasharray="3 2.5" fill="none"/></svg></div>
  <h3>MAINTAIN PRODUCT</h3>
  <p>We have the ability to quickly understand large, legacy products, write scaffold test cases around them</p>
</div>
<div class="abs svc" style="left:752px">
  <div class="ico-circle"><svg width="28" height="28" viewBox="0 0 24 24"><rect x="6" y="4" width="15" height="11" stroke="#fff" stroke-width="1.6" fill="none"/><circle cx="5" cy="14" r="2" fill="#fff"/><path d="M3 22v-4h5l4-4" stroke="#fff" stroke-width="1.6" fill="none"/></svg></div>
  <h3>HIGH END TRAINING</h3>
  <p>Our technical knowledge in languages such as C, C++, Java, .NET, LAMP stack, and Nodejs, as well as in dept...</p>
</div>
<a class="abs btn-red" style="left:511px;top:1047px;width:178px;height:36px">READ MORE SERVICES
  <svg width="14" height="10" viewBox="0 0 14 10"><path d="M0 5h12M8 1l4 4-4 4" stroke="#fff" stroke-width="2" fill="none"/></svg></a>

<!-- background & expertise -->
<section class="abs band"></section>
<h2 class="abs sec-title light" style="top:1220px">BACKGROUND AND EXPERTISE</h2>
<p class="abs sec-sub light" style="top:1261px">Perfection is achieved not when there is nothing more to add</p>
<p class="abs band-text">We are primarily server side programmers with expertise in large scale projects – be it Software development tools, Distributed software frameworks, Telecom and mediation software or Business intelligence. Over the years, we have been the trusted offshore product development partner for many startups and mid sized software product companies, and have built software products from scratch. We have built over 10 software products for startups all over the world. Best in class UI, and APIs have been designed and implemented by us.</p>
<a class="abs btn-white" style="left:199px;top:1432px;width:138px;height:36px">READ MORE
  <svg width="14" height="10" viewBox="0 0 14 10"><path d="M0 5h12M8 1l4 4-4 4" stroke="#c8141c" stroke-width="2" fill="none"/></svg></a>

<!-- engagement -->
<h2 class="abs sec-title" style="top:1603px">ENGAGEMENT MODELS</h2>
<p class="abs sec-sub" style="top:1645px">Perfection is achieved not when there is nothing more to add</p>
<div class="abs eng" style="left:199px">
  <div class="eng-ico"><svg width="34" height="34" viewBox="0 0 24 24"><circle cx="12" cy="12" r="3" fill="#fff"/><path d="M12 2v6M12 16v6M2 12h6M16 12h6M5 5l4 4M15 15l4 4M19 5l-4 4M9 15l-4 4" stroke="#fff" stroke-width="2"/></svg></div>
  <div><h3>OPD</h3><p>We provide pure Outsourced product development for either new software.....</p></div>
</div>
<div class="abs eng" style="left:477px">
  <div class="eng-ico"><svg width="36" height="36" viewBox="0 0 24 24" fill="#fff"><circle cx="12" cy="6" r="2.5"/><path d="M9 10h6v5H9z"/><circle cx="5" cy="13" r="2"/><circle cx="19" cy="13" r="2"/><path d="M3 16h4v5H3zM17 16h4v5h-4zM10 16h4v5h-4z"/></svg></div>
  <div><h3>BOT</h3><p>We help in setting up a team in India, gather expertise in your product and domain....</p></div>
</div>
<div class="abs eng" style="left:754px">
  <div class="eng-ico"><svg width="36" height="36" viewBox="0 0 24 24" fill="#fff"><circle cx="7" cy="5" r="2.2"/><circle cx="17" cy="5" r="2.2"/><path d="M5 8h4v14H5zM15 8h4v14h-4z"/><path d="M10 9h4v6h-4z"/></svg></div>
  <div><h3>EQUITY BASED</h3><p>If you are a startup with very strong growth potential, we are interested..</p></div>
</div>

<!-- case studies -->
<section class="abs cases" role="img" aria-label="Photo of a laptop, notebook and phone on a desk, shown in grey tones"></section>
<h2 class="abs sec-title light" style="top:1944px">CASE STUDIES</h2>
<p class="abs sec-sub light" style="top:1987px">Perfection is achieved not when there is nothing more to add</p>
<div class="abs case" style="left:199px;width:394px">
  <svg width="24" height="22" viewBox="0 0 24 22" style="flex:none"><path d="M12 1 1 6l11 5 11-5zM1 11l11 5 11-5M1 16l11 5 11-5" stroke="#fff" stroke-width="1.6" fill="none"/></svg>
  <div><h3>Automation for VARs – New product development</h3>
  <p>FlowVend is a complete automation system for VARs – it has an ecommerce storefront.....</p>
  <div class="more">READ MORE <svg width="14" height="10" viewBox="0 0 14 10"><path d="M0 5h12M8 1l4 4-4 4" stroke="#fff" stroke-width="2" fill="none"/></svg></div></div>
</div>
<div class="abs case" style="left:609px;width:392px">
  <svg width="24" height="22" viewBox="0 0 24 22" style="flex:none"><path d="M12 1 1 6l11 5 11-5zM1 11l11 5 11-5M1 16l11 5 11-5" stroke="#fff" stroke-width="1.6" fill="none"/></svg>
  <div><h3>Data center asset tracking product..</h3>
  <p>RackTrack Smart is an asset tracking and spares system built completely from the ground up to track servers..</p>
  <div class="more">READ MORE <svg width="14" height="10" viewBox="0 0 14 10"><path d="M0 5h12M8 1l4 4-4 4" stroke="#fff" stroke-width="2" fill="none"/></svg></div></div>
</div>
<div class="abs dots"><span class="on"></span><span></span><span></span></div>

<!-- blog -->
<h2 class="abs sec-title" style="top:2451px">Our Latest Blog</h2>
<p class="abs sec-sub" style="top:2493px">Perfection is achieved not when there is nothing more to add</p>
<article class="abs post" style="left:199px">
  <div class="post-tab"><svg width="30" height="30" viewBox="0 0 24 24"><path d="M4 3h16v12H10l-4 4v-4H4z" stroke="#c8141c" stroke-width="2" fill="none"/><path d="M8 7h8M8 11h5" stroke="#c8141c" stroke-width="2"/></svg></div>
  <p>Lorem Ipsum is simply dummy text the printing and typesetting..</p><hr><div class="date">4 Nov-17</div>
</article>
<article class="abs post" style="left:475px">
  <div class="post-tab"><svg width="30" height="30" viewBox="0 0 24 24"><path d="M4 3h16v12H10l-4 4v-4H4z" stroke="#c8141c" stroke-width="2" fill="none"/><path d="M8 7h8M8 11h5" stroke="#c8141c" stroke-width="2"/></svg></div>
  <p>Lorem Ipsum is simply dummy text the printing and typesetting..</p><hr><div class="date">4 Nov-17</div>
</article>
<article class="abs post" style="left:751px">
  <div class="post-tab"><svg width="30" height="30" viewBox="0 0 24 24"><path d="M4 3h16v12H10l-4 4v-4H4z" stroke="#c8141c" stroke-width="2" fill="none"/><path d="M8 7h8M8 11h5" stroke="#c8141c" stroke-width="2"/></svg></div>
  <p>Lorem Ipsum is simply dummy text the printing and typesetting..</p><hr><div class="date">4 Nov-17</div>
</article>
<a class="abs btn-red" style="left:262px;top:2722px;width:124px;height:38px">READ MORE <svg width="14" height="10" viewBox="0 0 14 10"><path d="M0 5h12M8 1l4 4-4 4" stroke="#fff" stroke-width="2" fill="none"/></svg></a>
<a class="abs btn-red" style="left:538px;top:2722px;width:124px;height:38px">READ MORE <svg width="14" height="10" viewBox="0 0 14 10"><path d="M0 5h12M8 1l4 4-4 4" stroke="#fff" stroke-width="2" fill="none"/></svg></a>
<a class="abs btn-red" style="left:814px;top:2722px;width:124px;height:38px">READ MORE <svg width="14" height="10" viewBox="0 0 14 10"><path d="M0 5h12M8 1l4 4-4 4" stroke="#fff" stroke-width="2" fill="none"/></svg></a>

<!-- footer -->
<footer class="abs footer">
  <div class="abs" style="left:199px;top:48px;width:240px">
    <div class="foot-h">About Us</div>
    <p class="foot-p" style="margin-top:14px">We are seasoned programmers, interested in the science as well as the craft of programming. We need to put high res black and white photos of Arvind – followed by a paragraph about Arvind. Ditto with Ravi and DM.</p>
  </div>
  <div class="abs" style="left:510px;top:48px">
    <div class="foot-h">Social Links</div>
    <ul class="soc-list" style="margin-top:8px">
      <li><span></span>Facenet</li><li><span></span>Chirper</li><li><span></span>Pinboard</li><li><span></span>Searchly</li>
    </ul>
  </div>
  <div class="abs" style="left:668px;top:48px">
    <div class="foot-h">Navigation</div>
    <ul class="foot-list" style="margin-top:8px">
      <li>POC</li><li>Build product</li><li>Maintain product</li><li>ODC setup</li><li>Architectural interventions</li><li>Agile Consulting</li>
    </ul>
  </div>
  <div class="abs" style="left:884px;top:72px">
    <ul class="foot-list">
      <li>SMEs</li><li>High end Training</li><li>Custom Development</li><li>Predictive Analytics</li>
    </ul>
  </div>
</footer>
<div class="abs copy">© Copyright 2017 brivoltsoftware-example. All Rights Reserved.</div>

</body>
</html>
```